Generative AI radar Infographics

I want to create an infographic called "Automated Reasoning Horizon Chart for Tender Replies". (see slide 3 of the PowerPoint file). I want to use it on social media (Pellocast and Website). I added 2 inspiration graphics in my brief (see slide 2 of the PowerPoint). I want to add my logo on the infographic. (I also uploaded my company logos). You can find model detailed instructions on slide 1 of the PowerPoint.
Target Market(s)
Business development and sales
Industry/Entity Type
I am a business consultant. I will be using this infographics on Pellocast and in my powerpoint presentations to clients
Look and feel
Each slider illustrates characteristics of the customer's brand and the style your logo design should communicate.

```html
<!DOCTYPE html>
<html lang="en">
<head>
<meta charset="utf-8">
<title>Automated Reasoning Horizon Chart for Tender Replies</title>
<link rel="stylesheet" href="https://fonts.googleapis.com/css2?family=Outfit:wght@400;500&family=Libre+Caslon+Text:wght@400&display=swap">
<style>
  :root{
    --blue:#0a93bd;
    --navy:#0b2f45;
    --grey-light:#a3a3a3;
    --grey-dark:#707070;
    --text-light:#a6a6a6;
    --text-dark:#7d7d7d;
    --dash:#9a9a9a;
    --bg:#ffffff;
  }
  *{margin:0;padding:0;box-sizing:border-box}
  html,body{width:1200px;height:675px;overflow:hidden;background:var(--bg)}
  .canvas{position:relative;width:1200px;height:675px;font-family:"Outfit",sans-serif}
  .title{position:absolute;left:57px;top:48px;font-size:22.5px;line-height:27px;font-weight:400;color:var(--navy)}
  .radar{position:absolute;left:0;top:0}
  .serif-label{font-family:"Libre Caslon Text",serif;font-size:18px;letter-spacing:.5px;fill:var(--navy)}
  .axis-note{font-family:"Outfit",sans-serif;font-size:10.5px;fill:var(--navy)}
  .band-label{font-family:"Outfit",sans-serif;font-size:14px;fill:#fff;letter-spacing:.3px}
  .item{position:absolute;display:flex;gap:4px;font-size:11px;line-height:11.5px;white-space:nowrap}
  .item .dot{flex:none;width:5px;height:5px;border-radius:50%;margin-top:3.5px}
  .item.right{text-align:right}
  .decision{color:var(--blue)} .decision .dot{background:var(--blue)}
  .development{color:var(--navy)} .development .dot{background:var(--navy)}
  .capture{color:var(--text-light)} .capture .dot{background:var(--grey-dark)}
  .strategy{color:var(--text-dark)} .strategy .dot{background:var(--grey-dark)}
  .brand{position:absolute;left:63px;top:603px;font-size:18px;font-weight:500;color:var(--navy);letter-spacing:.4px}
</style>
</head>
<body>
<div class="canvas">
  <h1 class="title">Automated Reasoning<br>Horizon Chart for<br>Tender Replies</h1>

  <svg class="radar" width="1200" height="675" viewBox="0 0 1200 675">
    <defs>
      <path id="arc-top" d="M420.1,123.2 A283 283 0 0 1 783.9,123.2"/>
      <path id="arc-bottom" d="M411.8,566.7 A296 296 0 0 0 792.2,566.7"/>
      <path id="arc-decision" d="M365.9,319.3 A237 237 0 0 1 581.3,103.9"/>
      <path id="arc-development" d="M622.7,103.9 A237 237 0 0 1 838.1,319.3"/>
      <path id="arc-capture" d="M581.3,576.1 A237 237 0 0 1 365.9,360.7"/>
      <path id="arc-strategy" d="M623.5,586.1 A247 247 0 0 0 848.1,361.5"/>
    </defs>

    <circle class="orbit" cx="602" cy="340" r="321" fill="none" stroke="var(--dash)" stroke-width="1" stroke-dasharray="5 4"/>

    <g class="bands">
      <path d="M337,335.4 A265 265 0 0 1 597.4,75 L598.2,120 A220 220 0 0 0 382,336.2 Z" fill="var(--blue)"/>
      <path d="M606.6,75 A265 265 0 0 1 867,335.4 L822,336.2 A220 220 0 0 0 605.8,120 Z" fill="var(--navy)"/>
      <path d="M867,344.6 A265 265 0 0 1 606.6,605 L605.8,560 A220 220 0 0 0 822,343.8 Z" fill="var(--grey-dark)"/>
      <path d="M597.4,605 A265 265 0 0 1 337,344.6 L382,343.8 A220 220 0 0 0 598.2,560 Z" fill="var(--grey-light)"/>
    </g>

    <g class="arrows" fill="#fff">
      <path d="M602,72 L590,92 L599,92 L599,110 L605,110 L605,92 L614,92 Z"/>
      <path d="M334,340 L354,328 L354,337 L372,337 L372,343 L354,343 L354,352 Z"/>
      <path d="M870,340 L850,328 L850,337 L832,337 L832,343 L850,343 L850,352 Z"/>
      <path d="M602,608 L590,588 L599,588 L599,570 L605,570 L605,588 L614,588 Z"/>
    </g>

    <text class="band-label"><textPath href="#arc-decision" startOffset="50%" text-anchor="middle">Decision Support</textPath></text>
    <text class="band-label"><textPath href="#arc-development" startOffset="50%" text-anchor="middle">Proposal Development</textPath></text>
    <text class="band-label"><textPath href="#arc-capture" startOffset="50%" text-anchor="middle">Capture Strategy</textPath></text>
    <text class="band-label"><textPath href="#arc-strategy" startOffset="50%" text-anchor="middle">Proposal Strategy</textPath></text>

    <text class="serif-label"><textPath href="#arc-top" startOffset="50%" text-anchor="middle">PROCESS ENHANCEMENT</textPath></text>
    <text class="serif-label"><textPath href="#arc-bottom" startOffset="50%" text-anchor="middle">STRATEGY ENABLEMENT</textPath></text>
    <text class="serif-label" x="318" y="333" text-anchor="middle" dominant-baseline="central" transform="rotate(-90 318 333)">INSIGHTS GENERATION</text>
    <text class="axis-note" x="332" y="328" text-anchor="middle" dominant-baseline="central" transform="rotate(-90 332 328)">(Transformative application)</text>
    <text class="serif-label" x="889" y="323" text-anchor="middle" dominant-baseline="central" transform="rotate(90 889 323)">TASK AUTOMATION</text>
    <text class="axis-note" x="875" y="323" text-anchor="middle" dominant-baseline="central" transform="rotate(90 875 323)">(foundational use)</text>

    <g class="petals">
      <path d="M598,336 L532,336 A66 66 0 0 1 586,271 Q597,266 598,254 Z" fill="var(--blue)"/>
      <path d="M598,336 L532,336 A66 66 0 0 1 586,271 Q597,266 598,254 Z" fill="var(--navy)" transform="rotate(90 602 340)"/>
      <path d="M598,336 L532,336 A66 66 0 0 1 586,271 Q597,266 598,254 Z" fill="var(--grey-dark)" transform="rotate(180 602 340)"/>
      <path d="M598,336 L532,336 A66 66 0 0 1 586,271 Q597,266 598,254 Z" fill="var(--grey-light)" transform="rotate(270 602 340)"/>
    </g>

    <g class="icons" fill="none" stroke="#fff" stroke-width="2" stroke-linecap="round" stroke-linejoin="round">
      <path d="M564,320 L590,320 M564,320 L569,315 M564,320 L569,325 M590,320 L585,315 M590,320 L585,325"/>
      <path d="M577,300 L577,312"/>
      <g fill="#fff" stroke="none">
        <rect x="626" y="312" width="6" height="12"/>
        <rect x="635" y="305" width="6" height="19"/>
        <rect x="644" y="298" width="6" height="26"/>
      </g>
      <path d="M625,304 L640,292 M640,292 L634,292 M640,292 L640,298"/>
      <path d="M566,362 L566,358 L570,358 M586,358 L590,358 L590,362 M590,378 L590,382 L586,382 M570,382 L566,382 L566,378"/>
      <rect x="571" y="361" width="14" height="18" rx="1"/>
      <path d="M574,366 L582,366 M574,370 L582,370 M574,374 L582,374"/>
      <path d="M640,356 L650,356 L655,361 L655,376 L640,376 Z"/>
      <path d="M643,364 L652,364 M643,368 L652,368 M643,372 L649,372"/>
      <path d="M623,382 L634,382 Q640,380 646,384 L656,378"/>
    </g>
  </svg>

  <div class="item decision" style="left:520px;top:146px"><span class="dot"></span><span>Bid/No Bid<br>Analysis</span></div>
  <div class="item decision" style="left:479px;top:180px"><span class="dot"></span><span>Bid Qualification</span></div>
  <div class="item decision" style="left:452px;top:200px"><span class="dot"></span><span>Opportunity<br>Assessment</span></div>
  <div class="item decision" style="left:427px;top:233px"><span class="dot"></span><span>Win Probability<br>modeling</span></div>
  <div class="item decision" style="left:412px;top:264px"><span class="dot"></span><span>Strategic Pricing<br>optimization</span></div>
  <div class="item decision" style="left:403px;top:301px"><span class="dot"></span><span>Compliance<br>Assessment</span></div>

  <div class="item right development" style="right:509px;top:144px"><span>Company profile</span><span class="dot"></span></div>
  <div class="item right development" style="right:487px;top:162px"><span>CV and Resumes</span><span class="dot"></span></div>
  <div class="item right development" style="right:459px;top:180px"><span>Past Performance</span><span class="dot"></span></div>
  <div class="item right development" style="right:440px;top:198px"><span>Technical solution</span><span class="dot"></span></div>
  <div class="item right development" style="right:425px;top:217px"><span>Compliance Matrix</span><span class="dot"></span></div>
  <div class="item right development" style="right:410px;top:236px"><span>Statement of Work</span><span class="dot"></span></div>
  <div class="item right development" style="right:401px;top:256px"><span>Executive Summary</span><span class="dot"></span></div>
  <div class="item right development" style="right:395px;top:275px"><span>Security<br>Questionnaires</span><span class="dot"></span></div>
  <div class="item right development" style="right:387px;top:308px"><span>Due Diligence<br>Questionnaires</span><span class="dot"></span></div>

  <div class="item capture" style="left:406px;top:375px"><span class="dot"></span><span>Capture Plan</span></div>
  <div class="item capture" style="left:411px;top:394px"><span class="dot"></span><span>SWOT Analysis</span></div>
  <div class="item capture" style="left:419px;top:414px"><span class="dot"></span><span>Customer<br>Hot Buttons</span></div>
  <div class="item capture" style="left:436px;top:444px"><span class="dot"></span><span>Customer<br>Intelligence</span></div>
  <div class="item capture" style="left:464px;top:473px"><span class="dot"></span><span>Competitive<br>Intelligence</span></div>
  <div class="item capture" style="left:500px;top:501px"><span class="dot"></span><span>Value<br>Proposition</span></div>

  <div class="item right strategy" style="right:398px;top:390px"><span>Proposal plan</span><span class="dot"></span></div>
  <div class="item right strategy" style="right:405px;top:409px"><span>Proposal outline</span><span class="dot"></span></div>
  <div class="item right strategy" style="right:420px;top:429px"><span>Differentiators</span><span class="dot"></span></div>
  <div class="item right strategy" style="right:436px;top:451px"><span>Win Theme<br>extraction</span><span class="dot"></span></div>
  <div class="item right strategy" style="right:461px;top:479px"><span>Key messages<br>extraction</span><span class="dot"></span></div>

  <div class="brand">Quillmark Advisory Group</div>
</div>
</body>
</html>
```